Dorm Svc Mission Statement Graphic

We need an engaging and bold design that highlights our department's new mission statement. It must include our logo and department colors. It should also include the college logo. Dorm Svc logo standards are:
Blue is PMS 301C
Green is PMS 368C
Gray is PMS CGray9
"LVC" font is FF More Wide Black Italic
"Dormitory Services" font is sans serif Officina

College logo is PMS 301C

The text of our mission statement is:
Larkspur Valley College's Department of Dormitory Services strives to provide safe living environments, with a community that fosters personal growth and academic success; through a student centered foundation that encourages residents to recognize their potential and diversity.
We aim to build an accessible and sustainable lifestyle in the heart of the Colorado Rockies.

Industry/Entity Type

College

```html
<!DOCTYPE html>
<html lang="en">
<head>
<meta charset="utf-8">
<title>LVC Dormitory Services – Our Mission</title>
<link rel="stylesheet" href="https://fonts.googleapis.com/css2?family=Arimo:wght@700&family=EB+Garamond:wght@500&display=swap">
<style>
  :root {
    --blue: #004b87;
    --blue-deep: #0a3361;
    --blue-mid: #0d5aa0;
    --green: #78be20;
    --green-deep: #3f7f12;
    --gray: #75787b;
    --paper: #ffffff;
    --stage: #e4e4e4;
  }
  * { margin: 0; padding: 0; box-sizing: border-box; }
  html, body {
    width: 1200px; height: 1000px; overflow: hidden;
    background: var(--stage);
  }
  .poster {
    position: absolute; left: 267px; top: 30px;
    width: 665px; height: 940px;
    background: var(--paper);
    overflow: hidden;
    box-shadow: 0 2px 10px rgba(0,0,0,.18);
  }
  .header-band { position: absolute; left: 0; top: 0; width: 665px; height: 190px; }
  .brand {
    position: absolute; left: 405px; top: 52px; width: 230px;
    font-family: "Arimo", Arial, sans-serif; font-weight: 700;
    color: var(--blue); text-align: center; line-height: 1;
  }
  .brand-mark { display: block; font-size: 64px; letter-spacing: 2px; }
  .brand-sub { display: block; font-size: 20px; margin-top: 6px; }
  .photo-area {
    position: absolute; left: 0; top: 290px; width: 665px; height: 640px;
    background:
      radial-gradient(ellipse 55% 40% at 40% 25%, rgba(255,255,235,.95), rgba(255,255,235,0) 70%),
      linear-gradient(180deg, #dfe9c2 0%, #c9dc92 40%, #b4d04a 60%, #c6d82e 78%, #d7df5a 100%);
    -webkit-mask-image: linear-gradient(180deg, transparent 0%, #000 14%, #000 80%, transparent 100%);
    mask-image: linear-gradient(180deg, transparent 0%, #000 14%, #000 80%, transparent 100%);
  }
  .mission-title {
    position: absolute; left: 0; top: 165px; width: 665px; text-align: center;
    font-family: "EB Garamond", Georgia, serif; font-weight: 500;
    font-size: 30px; color: var(--blue); letter-spacing: .5px;
  }
  .mission-text {
    position: absolute; left: 90px; top: 215px; width: 485px; text-align: center;
    font-family: "Arimo", Arial, sans-serif; font-weight: 700;
    font-size: 16px; line-height: 24.5px; color: var(--blue); white-space: nowrap;
  }
  .aim-quote {
    position: absolute; left: 131px; top: 620px; width: 480px;
    font-family: "Arimo", Arial, sans-serif; font-weight: 700;
    font-size: 28px; line-height: 41px; color: var(--blue); white-space: nowrap;
    text-shadow: 0 0 3px rgba(255,255,255,.9), 0 0 1px #fff;
  }
  .quote-mark {
    position: absolute; font-family: Georgia, serif; font-weight: 700;
    font-size: 50px; color: var(--blue); line-height: 1;
  }
  .quote-open { left: 108px; top: 605px; }
  .quote-close { left: 578px; top: 722px; }
  .college {
    position: absolute; left: 0; top: 800px; width: 665px; height: 140px;
  }
  .college-square {
    position: absolute; left: 160px; top: 20px; width: 56px; height: 56px;
    background: var(--blue);
  }
  .college-name {
    position: absolute; left: 231px; top: 12px;
    font-family: "EB Garamond", Georgia, serif; font-weight: 500;
    font-size: 38px; color: var(--blue); white-space: nowrap;
  }
  .college-dept {
    position: absolute; left: 232px; top: 64px;
    font-family: "Arimo", Arial, sans-serif; font-weight: 700;
    font-size: 16px; letter-spacing: 3.6px; color: var(--green-deep); white-space: nowrap;
  }
</style>
</head>
<body>
  <main class="poster">
    <div class="photo-area" role="img" aria-label="Photo of students playing together on a sunlit lawn beneath tall trees"></div>

    <svg class="header-band" viewBox="0 0 665 190" aria-hidden="true">
      <defs>
        <linearGradient id="band-blue" x1="0" y1="0" x2="1" y2="0">
          <stop offset="0" stop-color="var(--blue-deep)"/>
          <stop offset="1" stop-color="var(--blue-mid)"/>
        </linearGradient>
        <linearGradient id="band-green" x1="0" y1="0" x2="1" y2="1">
          <stop offset="0" stop-color="var(--green)"/>
          <stop offset="1" stop-color="var(--green-deep)"/>
        </linearGradient>
      </defs>
      <rect x="0" y="0" width="665" height="190" fill="url(#band-blue)"/>
      <path d="M220 0 H665 V190 H205 C210 120 225 60 262 0 Z" fill="var(--gray)"/>
      <path d="M278 0 H665 V190 H240 C245 120 255 55 300 0 Z" fill="url(#band-green)"/>
      <path d="M0 92 C150 62 330 56 470 116 C545 146 615 146 665 128 V190 H0 Z" fill="var(--paper)"/>
    </svg>

    <div class="brand">
      <span class="brand-mark">LVC</span>
      <span class="brand-sub">Dormitory Services</span>
    </div>

    <h1 class="mission-title">OUR MISSION</h1>
    <p class="mission-text">Strives to provide safe living environments, with a<br>community that fosters personal growth and<br>academic success; through a student centered<br>foundation that encourages residents to recognize<br>their potential and diversity.</p>

    <span class="quote-mark quote-open">“</span>
    <p class="aim-quote">We aim to build an accessible<br>and sustainable lifestyle in the<br>heart of the Colorado Rockies.</p>
    <span class="quote-mark quote-close">”</span>

    <footer class="college">
      <span class="college-square"></span>
      <span class="college-name">Larkspur Valley College</span>
      <span class="college-dept">Department of Dormitory Services</span>
    </footer>
  </main>
</body>
</html>
```